Field Notes for Business Risk Advisors

I am writing a best practice book for commercial lines insurance brokers. The subtitle is Nobody Promised The Trail Was Flat. So I want a graphic of maybe someone hiking the summit. I posted an example but don't feel limited I just foudn something I liked.

This is a business book

I just mocked up an example. I dont want designers limited by my design. I am looking for juggling to be artistically displayed on the front cover. I incorporated my name into the logo but probably dont want that in my final design. Should just have my name and designations Marek Dallow, AAi, CWCP

Commercial Insurance Agents

Insurance

Sans Serif

• Must have the title of the book
Field Notes
for Business Risk
Advisors

Also the sub title Nobody Promised The Trail Was Flat

My Name on front cover Marek Dallow, AAI, CWCP

Book Cover should be black. I uploaded a copy of my work comp playbook for my desired color scehme.

My Lantern Logo on front cover and Tidewell logo on back cover
• Color should be black gray adn red using color from my logo.

```html
<!DOCTYPE html>
<html lang="en">
<head>
<meta charset="utf-8">
<title>Field Notes for Business Risk Advisors — Cover</title>
<link rel="stylesheet" href="https://fonts.googleapis.com/css2?family=Anton&family=Lato:wght@400;700&display=swap">
<style>
  :root {
    --page-bg: #f2f2f2;
    --sky-top: #5a82b4;
    --sky-light: #a9bfd6;
    --cloud: #eef0ef;
    --cloud-shade: #c9ced0;
    --horizon: #9eabb0;
    --fields: #5b6a3c;
    --fields-dark: #46532f;
    --rock-light: #9a8a62;
    --rock: #7b6c4d;
    --rock-dark: #3f3a30;
    --ink: #0b0b0b;
    --accent-red: #b3322b;
    --paper-white: #ffffff;
    --brand-ink: #1c1c1c;
  }
  * { margin: 0; padding: 0; box-sizing: border-box; }
  html, body { width: 1200px; height: 675px; overflow: hidden; background: var(--page-bg); }
  .stage { width: 1200px; height: 675px; display: flex; justify-content: center; align-items: center; }
  .cover {
    position: relative; width: 472px; height: 675px; overflow: hidden;
    font-family: "Lato", sans-serif; text-align: center;
  }
  .cover-scene {
    position: absolute; inset: 0;
    background: linear-gradient(180deg,
      var(--sky-top) 0%, var(--sky-light) 8%, var(--cloud) 18%,
      var(--cloud-shade) 30%, var(--cloud) 38%, var(--sky-light) 44%,
      var(--horizon) 48%, var(--fields) 55%, var(--fields-dark) 62%,
      var(--rock-light) 67%, var(--rock) 80%, var(--rock-dark) 100%);
  }
  .author {
    position: absolute; top: 34px; left: 0; right: 0;
    color: var(--accent-red); font-size: 34px; font-weight: 400;
    font-variant: small-caps; line-height: 1;
  }
  .title {
    position: absolute; top: 100px; left: 0; right: 0;
    font-family: "Anton", sans-serif; font-weight: 400; color: var(--ink);
    font-variant: small-caps; line-height: 1.05;
  }
  .title-line { display: block; font-size: 44px; letter-spacing: 0.5px; }
  .title-line--lead { font-size: 70px; line-height: 1; }
  .subtitle {
    position: absolute; top: 506px; left: 0; right: 0;
    color: var(--paper-white); font-size: 25px; font-weight: 700;
    font-variant: small-caps; line-height: 1;
  }
  .brand {
    position: absolute; top: 622px; left: 0; right: 0;
    display: flex; justify-content: center; align-items: center; gap: 10px;
    color: var(--brand-ink); font-size: 24px; font-weight: 400; letter-spacing: 8px;
    text-transform: uppercase; line-height: 1;
  }
  .brand-dot { width: 12px; height: 12px; border-radius: 50%; background: var(--accent-red); }
</style>
</head>
<body>
<main class="stage">
  <section class="cover">
    <div class="cover-scene" role="img" aria-label="Photo of a hiker with a backpack standing on a rocky summit, arms raised, overlooking farmland under a cloudy blue sky"></div>
    <p class="author">Marek Dallow, AAI, CWCP</p>
    <h1 class="title">
      <span class="title-line">Field Notes</span>
      <span class="title-line">for Business Risk</span>
      <span class="title-line title-line--lead">Advisors</span>
    </h1>
    <p class="subtitle">Nobody Promised The Trail Was Flat</p>
    <div class="brand"><span class="brand-dot"></span><span class="brand-name">Lantern</span></div>
  </section>
</main>
</body>
</html>
```